verdant terraces simple classy business card design

my name is owen harlow and I run a gardening business aimed at high class verdant terraces. the business name is verdant terraces and our logo was designed on pixel forum .My clientel are anything from residential homes to businesses. I take pride in my work and know that I offer a service like no other in my area.
The business card will be used to represent my business and I want it to be not only rememberable, but simplistic and modern. Eye catching too. Of course I would like it relatable to gardening and appealing to the correct clientel - those being garden enthusiasts, prestigious homes and businesses that are after top of the line gardening services like no other on the market.
I am not a typical lawn mowing business so I don't want a typical card design that represents that. The gardens I work with are generally million dollar properties with owners who are very garden proud looking for upkeep and guidance from me along with sometimes whole new garden designs. I want the business cards to show to my clients that I take pride, as they do, in their garden. And I want them to know from my card that I am a professional, qualified horticulturist offering them a top of the line service for life. I want them to refer my business on. I want them to look at my business card and see class and professionalism in a modern unique bold way.
The card should be simple with the possibility of the logo on the front being embossed/debossed and my details on the back the card should have a organic garden feel it's very important to me that it is absolutely perfect
I am also very open to ideas and suggestions so look forward to seeing the designs. the business logo has been supplied with this project and I want the card to be double sided

Contact info is
Owen Harlow - Managing Director / Horticulturist
Phone : 0481 526 704
Email: owenharlow@verdantterraces.com.au

Target Market(s)

high class gardens residential and commercial

Industry/Entity Type

Gardener

Contact Information for Business Card

Contact info is
Phone : 0481 526 704

PLEASE MAKE CARD DOUBLE SIDED

Requirements
Must have
• organic simple classy modern feel
• must flow with the current logo that has been supplied with this project
• Double sided
• Must explain in a simple way that I deal with high end gardens and I'm a qualified horticulturist
Nice to have
• embossed debossed logo
Should not have
• shouldn't be to busy or cheap looking

```html
<!DOCTYPE html>
<html lang="en">
<head>
<meta charset="utf-8">
<title>Verdant Terraces — Business Card</title>
<link rel="stylesheet" href="https://fonts.googleapis.com/css2?family=Montserrat:wght@400;500&display=swap">
<style>
  :root {
    --backdrop: #c8cecf;
    --card-stock: #f4f4f1;
    --card-edge: #b9a66a;
    --leaf-green: #2f8a3a;
    --ink: #2b2b2b;
    --ink-soft: #4a4a4a;
  }
  * { margin: 0; padding: 0; box-sizing: border-box; }
  html, body {
    width: 1200px;
    height: 1000px;
    overflow: hidden;
    background: var(--backdrop);
    font-family: "Montserrat", sans-serif;
  }
  .card-set {
    position: relative;
    width: 1200px;
    height: 1000px;
    display: flex;
    flex-direction: column;
    align-items: center;
    justify-content: center;
    gap: 60px;
  }
  .card {
    position: relative;
    width: 630px;
    height: 360px;
    background: var(--card-stock);
    border-bottom: 3px solid var(--card-edge);
    box-shadow: 0 10px 28px rgba(0, 0, 0, 0.12);
  }
  .brand {
    display: flex;
    align-items: center;
    color: var(--leaf-green);
  }
  .brand-mark {
    flex: none;
    border-radius: 50%;
    background: var(--leaf-green);
  }
  .brand-name {
    font-weight: 500;
    text-transform: uppercase;
    line-height: 1.1;
  }
  /* Front */
  .card-front .brand {
    position: absolute;
    inset: 0;
    justify-content: center;
    gap: 22px;
  }
  .card-front .brand-mark { width: 84px; height: 84px; }
  .card-front .brand-name { font-size: 34px; letter-spacing: 0.08em; }
  /* Back */
  .card-back .contact {
    position: absolute;
    left: 48px;
    top: 118px;
    color: var(--ink);
  }
  .contact-name { font-size: 24px; font-weight: 500; }
  .contact-role { font-size: 13px; color: var(--ink-soft); margin-top: 2px; }
  .contact-lines { list-style: none; margin-top: 14px; font-size: 13px; line-height: 1.6; }
  .card-back .brand {
    position: absolute;
    right: 44px;
    top: 118px;
    flex-direction: column;
    gap: 10px;
  }
  .card-back .brand-mark { width: 48px; height: 48px; }
  .card-back .brand-name { font-size: 18px; letter-spacing: 0.08em; text-align: center; }
</style>
</head>
<body>
  <main class="card-set">
    <section class="card card-front" aria-label="Card front">
      <div class="brand">
        <span class="brand-mark"></span>
        <span class="brand-name">Verdant<br>Terraces</span>
      </div>
    </section>

    <section class="card card-back" aria-label="Card back">
      <div class="contact">
        <h1 class="contact-name">Owen Harlow</h1>
        <p class="contact-role">Managing Director / Horticulturist</p>
        <ul class="contact-lines">
          <li>P : 0481 526 704</li>
          <li>E : owenharlow@verdantterraces.com.au</li>
        </ul>
      </div>
      <div class="brand">
        <span class="brand-mark"></span>
        <span class="brand-name">Verdant<br>Terraces</span>
      </div>
    </section>
  </main>
</body>
</html>
```